BKT Consulting

Government/Entitlement Consulting Services- I assist developers obtain entitlements from local, state and federal government agencies so that they can build their projects. Often these projects are very complicated and political and may face community opposition.

Target Market(s)

Real Estate Developers

Industry/Entity Type

Business Consultant

Contact Information for Business Card

Dana Velmonte
Principal

Font styles to use
Serif
Sans Serif

Requirements
Must have
• Classy and professional appeal.
Nice to have
• I like a combination of a mat and glossy finish. I've seen that done with black and then a bold color for a pop, but am not 100% committed to that.

```html
<!DOCTYPE html>
<html lang="en">
<head>
<meta charset="utf-8">
<title>BKT Consulting – Business Card</title>
<link rel="stylesheet" href="https://fonts.googleapis.com/css2?family=Open+Sans:wght@400;600&family=Crimson+Text:wght@400&display=swap">
<style>
  :root {
    --backdrop: #c9cecc;
    --paper: #f1f0ec;
    --gold: #8c6f1f;
    --gold-soft: #9b7f2e;
    --edge: #a68a3a;
  }
  * { margin: 0; padding: 0; box-sizing: border-box; }
  html, body {
    width: 1200px;
    height: 823px;
    overflow: hidden;
    background: var(--backdrop);
  }
  .canvas {
    position: relative;
    width: 1200px;
    height: 823px;
  }
  .card {
    position: absolute;
    top: 261px;
    width: 520px;
    height: 300px;
    background: var(--paper);
    border-bottom: 4px solid var(--edge);
    box-shadow: 0 10px 30px rgba(60, 66, 64, 0.18);
  }
  .card--back { left: 50px; }
  .card--front { left: 630px; }

  .wordmark {
    font-family: "Open Sans", sans-serif;
    font-weight: 600;
    color: var(--gold);
    letter-spacing: 0.02em;
    display: flex;
    align-items: center;
    gap: 12px;
    white-space: nowrap;
  }
  .wordmark__square {
    width: 0.8em;
    height: 0.8em;
    background: var(--gold);
  }
  .card--front .wordmark {
    position: absolute;
    left: 50%;
    top: 50%;
    transform: translate(-50%, -50%);
    font-size: 44px;
  }
  .card--back .wordmark {
    position: absolute;
    left: 36px;
    top: 44px;
    font-size: 30px;
  }

  .contact {
    position: absolute;
    right: 36px;
    top: 110px;
    text-align: right;
    color: var(--gold-soft);
  }
  .contact__name {
    font-family: "Open Sans", sans-serif;
    font-weight: 600;
    font-size: 19px;
    letter-spacing: 0.2em;
    text-transform: uppercase;
    color: var(--gold);
  }
  .contact__title {
    font-family: "Open Sans", sans-serif;
    font-size: 10px;
    letter-spacing: 0.2em;
    text-transform: uppercase;
    margin-top: 2px;
  }
  .contact__block {
    font-family: "Crimson Text", serif;
    font-size: 16px;
    line-height: 1.15;
    margin-top: 12px;
  }
</style>
</head>
<body>
  <main class="canvas">
    <section class="card card--back" aria-label="Card back with contact details">
      <div class="wordmark"><span class="wordmark__square"></span>BKT Consulting</div>
      <div class="contact">
        <p class="contact__name">Dana Velmonte</p>
        <p class="contact__title">Principal</p>
        <p class="contact__block">56 Market Row<br>Riverton 0000</p>
        <p class="contact__block">(000)-000-0000<br>(000)-000-0000<br>hello@bktconsulting.com<br>www.bktconsulting.com</p>
      </div>
    </section>
    <section class="card card--front" aria-label="Card front">
      <div class="wordmark"><span class="wordmark__square"></span>BKT Consulting</div>
    </section>
  </main>
</body>
</html>
```